Flyer-Design für europäisches Forschungsprojekt
Beschreibung
Bei diesem Projekt handelt es sich um ein europäisches Forschungsprojekt aus dem Bereich Telekommunikation.
Ziel
The MELOTRA project plans to bring together a novel high frequency advanced radio architecture and an Artificial Intelligence (AI) network processing and management approach into a new type of intelligent communications system Beyond 5G. The new intelligent system approach is necessary because the scale and complexity of the new radio attributes in the new frequency ranges cannot be optimally operated using traditional network management approaches.
Allgemeine Informationen zum Thema:
Projekt Website: http://vbn-melotra.eu
Aufgabenstellung
Wir möchten einen professionellen Flyer, der über das Projekt und seine Zielsetzungen informiert. Zielgruppe sind Fachleute aus diesem Forschungsbereich und Projektteilnehmer.
Sprachliche Anforderung
Projektsprache ist Englisch.
In den Dateien befindet sich eine Word-Datei, die einen Überblick über die Inhalte liefern soll.
Lediglich die enthaltenen Text-Informationen sind 1:1 zu übernehmen, ebenso müssen die Grafiken verwendet werden. Wichtig ist eine vollständige Aufnahme der am Projekt beteiligten Partner in Form ihrer Logos. Ebenso muss eine EU Flagge enthalten sein, sowie das Melotra-Projektlogo.
Die gesamte Gestaltung und Anordnung der Informationen ist selbstverständlich Ihnen überlassen.
Der Flyer sollte übliche DIN Maße haben. Bitte rechnen sie mind. 1 mm Beschnitt auf jeder Außenseite ein. Die Anzahl der Seiten (und Falzen) ist Ihnen überlassen.
Wichtig ist, dass wir nachbearbeitbare Roh-Dateien erhalten. (Z.B: .ai, .eps, .indd )
Wir freuen uns auf Ihre kreativen Vorschläge.

```html
<!DOCTYPE html>
<html lang="en">
<head>
<meta charset="utf-8">
<title>MELOTRA Flyer</title>
<link rel="stylesheet" href="https://fonts.googleapis.com/css2?family=Nunito+Sans:wght@300;400;600;700&display=swap">
<style>
:root{
  --bg:#eceae6;
  --paper:#fbfcfb;
  --panel-grey:#dfe1e2;
  --teal:#3f97a0;
  --teal-line:#9cc9cd;
  --ink:#2f3336;
  --muted:#5b6166;
  --cover-top:#1d2740;
  --cover-mid:#3c5675;
  --cover-low:#8a7a55;
  --pink:#f3b7b1;
  --green:#bddf9c;
  --violet:#d2c5e6;
  --cyan:#d3f0f3;
  --grey-cell:#e4e6e8;
}
*{box-sizing:border-box;margin:0;padding:0}
html,body{width:1200px;height:900px;overflow:hidden}
body{background:var(--bg);font-family:"Nunito Sans",sans-serif;color:var(--ink);position:relative}
.flyer-side{position:absolute;left:45px;width:1110px;height:400px;background:var(--paper);display:flex;box-shadow:0 2px 8px rgba(0,0,0,.12)}
.flyer-side.outside{top:40px}
.flyer-side.inside{top:460px}
.panel{position:relative;width:370px;height:400px;padding:14px 16px}
.panel.grey{background:var(--panel-grey)}
.section-label{color:var(--teal);font-size:7px;border-bottom:1px solid var(--teal-line);padding-bottom:3px;margin-bottom:12px}
h2{font-size:8.6px;font-weight:700;margin-bottom:8px}
h3{font-size:8.4px;font-weight:700;margin:12px 0 6px}
p,li{font-size:7.6px;line-height:1.3}
.body-text{color:var(--muted)}
.contact{position:absolute;left:16px;right:16px;top:200px}
.contact p{margin-bottom:7px}
.contact b{font-weight:700;color:var(--ink)}
.footer-rule{position:absolute;left:0;right:0;bottom:32px;border-top:1px solid var(--teal-line)}
.brand{display:flex;align-items:center;gap:5px;color:var(--teal);font-weight:300;letter-spacing:1px}
.brand .dot{width:11px;height:11px;border-radius:50%;background:var(--teal);opacity:.8}
.panel-brand{position:absolute;right:14px;bottom:8px;font-size:17px}
.partner-grid{display:grid;grid-template-columns:1fr 1fr;row-gap:18px;column-gap:14px;margin-top:6px}
.partner{display:flex;align-items:center;gap:6px;font-size:9px;font-weight:600;color:var(--muted);height:22px;padding-left:20px}
.partner i{width:12px;height:12px;background:var(--teal-line);display:block}
.disclaimer{position:absolute;left:16px;right:16px;top:290px}
.funding-marks{display:flex;gap:14px;align-items:center;margin-bottom:12px}
.eu-badge{width:46px;height:28px;background:#2f5fa8}
.funding-name{font-size:10px;font-weight:600;color:#4d4fa0}
.cover{padding:0}
.cover-image{height:300px;background:linear-gradient(180deg,var(--cover-top) 0%,var(--cover-mid) 55%,var(--cover-low) 100%)}
.cover-title{position:absolute;top:36px;left:55px;right:55px;text-align:center;color:#f2f4f6;font-size:20px;line-height:1.25;font-weight:400}
.cover-brand{position:absolute;bottom:32px;left:0;right:0;justify-content:center;font-size:31px;color:#5fa1a9}
.cover-brand .dot{width:24px;height:24px}
.objectives li{list-style:none;margin-bottom:6px}
.pillars-title{position:absolute;right:16px;top:14px;font-size:7px;color:var(--teal)}
.pillars-table{position:absolute;left:385px;top:40px;width:520px;height:150px;border:1px solid #c9cfd2;display:grid;grid-template-columns:72px 1fr 1fr 1fr 42px;gap:4px;padding:6px;background:#fff}
.col{display:flex;flex-direction:column;gap:6px;border-radius:8px;padding:4px 3px}
.col .head{font-size:5.6px;font-weight:700;text-align:center;height:10px}
.cell{flex:1;font-size:4.6px;line-height:1.3;text-align:center;display:flex;align-items:center;justify-content:center;padding:2px}
.col.pillar .cell{background:var(--grey-cell);color:var(--muted)}
.col.objective{background:var(--pink)}
.col.action{background:var(--green)}
.col.action .cell{text-align:left;justify-content:flex-start}
.col.demo{background:var(--violet)}
.col.kpi{background:var(--cyan)}
.kpi-text{flex:1;writing-mode:vertical-rl;transform:rotate(180deg);font-size:4.6px;line-height:1.4;text-align:center}
.concept-figure{position:absolute;left:385px;top:202px;width:520px;height:150px;border:1px solid #c9cfd2;background:linear-gradient(135deg,#f6f1f0 0%,#eef3f4 50%,#f3eef0 100%)}
.caption{position:absolute;right:16px;font-size:8.4px;color:var(--teal);line-height:1.2;width:108px}
.caption.upper{top:185px}
.caption.lower{top:322px}
</style>
</head>
<body>

<section class="flyer-side outside">
  <div class="panel about">
    <div class="section-label">About</div>
    <h2>Adaptive Learning Assisted Sub-THz Network for Beyond 5G Evolution</h2>
    <p class="body-text">MELOTRA is a F2030 NetPact project which aims to bring together a novel high frequency advanced radio architecture and an AI network processing and management approach into a new type of intelligent communications system Beyond 5G. MELOTRA started in November 2019 and will run for 3 years.</p>
    <div class="contact">
      <div class="section-label">Contact</div>
      <p class="body-text"><b>Coordinator:</b> Joris Elmquist, Velmarox</p>
      <p class="body-text"><b>Technical Manager:</b> Sofia Maravelaki, Korinth Institute Research Centre</p>
      <p class="body-text" style="margin-top:12px"><b>Website:</b> https://www.vbn-melotra.eu/</p>
      <p class="body-text"><b>Chirper</b> @MelotraIct</p>
      <p class="body-text">https://chirper.net/MelotraIct?s=20</p>
      <p class="body-text"><b>Contact:</b> https://www.vbn-melotra.eu/contact/</p>
      <p class="body-text">or by mail to contact@vbn-melotra.eu</p>
    </div>
    <div class="footer-rule"></div>
    <div class="brand panel-brand"><span class="dot"></span>MELOTRA</div>
  </div>

  <div class="panel partners">
    <div class="section-label">Partners</div>
    <div class="partner-grid">
      <div class="partner"><i></i>Tessaron</div>
      <div class="partner"><i></i>Lindquelle</div>
      <div class="partner"><i></i>Korinth Inst.</div>
      <div class="partner"><i></i>Sciencia</div>
      <div class="partner"><i></i>Varnok</div>
      <div class="partner"><i></i>Datadrift</div>
      <div class="partner"><i></i>Atomeion</div>
      <div class="partner"><i></i>Telvoria</div>
      <div class="partner"><i></i>Velmarox</div>
      <div class="partner"><i></i>Rannikko Univ.</div>
      <div class="partner"><i></i>Pohjola Univ.</div>
      <div class="partner"><i></i>Tecnicava</div>
    </div>
    <div class="disclaimer">
      <div class="section-label">Disclaimer</div>
      <div class="funding-marks">
        <div class="eu-badge" role="img" aria-label="Blue funding programme flag"></div>
        <span class="funding-name">NetPact</span>
      </div>
      <p class="body-text">This project has received funding from the Frontier 2030 Programme under grant agreement number 905317 – MELOTRA</p>
    </div>
  </div>

  <div class="panel cover">
    <div class="cover-image" role="img" aria-label="Night view of the Earth from space with a glowing network mesh over the city lights"></div>
    <h1 class="cover-title">Adaptive Learning Assisted Sub-THz Network for Beyond 5G Evolution</h1>
    <div class="brand cover-brand"><span class="dot"></span>MELOTRA</div>
  </div>
</section>

<section class="flyer-side inside">
  <div class="panel grey objectives">
    <div class="section-label">Objectives and Vision</div>
    <h2>The MELOTRA Pillars</h2>
    <ol>
      <li>1. Develop new radio technologies for communications using the above 100Ghz D-Band frequency ranges.</li>
      <li>2. Exploit emerging advanced connectivity approaches based on metasurfaces and shaping propagation environments in D-band</li>
      <li>3. Employ Artificial Intelligence to high-frequency communications resource management with dynamic assignment and reconfiguration of metasurfaces to provide continuous and reliable high-bandwidth connections in a Beyond-5G scenari</li>
    </ol>
    <h3>MELOTRA - Objectives and Vision</h3>
    <ul>
      <li>• Aspires bringing 5G wireless thinking to a long term vision of pervasive mobile virtual services, with computing and connectivity functions managed in an integrated way</li>
      <li>• Envisions a unified system beyond 5G, bringing together a novel high frequency advanced radio architecture with an Artificial Intelligence network processing and management approach</li>
      <li>• Aims to implement and showcase a PoC of a beyond 5G wireless communications networks concept addressing machine learning based dynamic ultra-high spectral efficient and reliable communications in the bandwidth-rich D-band and intelligent network management in both “Line of Sight” (LOS) and “Non-Line of Sight” (NLOS) environments</li>
    </ul>
    <div class="footer-rule"></div>
  </div>
  <div class="panel">
    <div class="footer-rule"></div>
  </div>
  <div class="panel">
    <div class="pillars-title">The MELOTRA Pillars</div>
    <div class="caption upper">MELOTRA system concept for networks beyond 5G</div>
    <div class="caption lower">MELOTRA system concept for networks beyond 5G</div>
    <div class="footer-rule"></div>
    <div class="brand panel-brand"><span class="dot"></span>MELOTRA</div>
  </div>

  <div class="pillars-table">
    <div class="col pillar">
      <div class="head">Pillars</div>
      <div class="cell">D-band for 100 Gbit/s reliable wireless connectivity</div>
      <div class="cell">Communications beyond the Shannon paradigm</div>
      <div class="cell">Artificial Intelligence-based wireless system concept</div>
    </div>
    <div class="col objective">
      <div class="head">Objectives</div>
      <div class="cell">100 Gbit/s capable, energy and spectral-efficient D-Band wireless B5G networks</div>
      <div class="cell">Ultra-reliable D-band connectivity and reconfigurability in all usage environments</div>
      <div class="cell">Transform networks B5G into intelligent connectivity/computing platforms</div>
    </div>
    <div class="col action">
      <div class="head">Actions</div>
      <div class="cell">• D-band front-end<br>• Baseband DSP<br>• Adaptive spatial SP<br>• High gain D-band antennas<br>• Channel modelling</div>
      <div class="cell">• Reconfigurable adaptive metasurface design<br>• Beamforming for LOS and NLOS links<br>• MAC design</div>
      <div class="cell">• ML for channel modelling<br>• ML-based resource allocation and energy efficiency ML for network deployment optimization</div>
    </div>
    <div class="col demo">
      <div class="head">Demos</div>
      <div class="cell">P2P D-band LOS outdoor demo</div>
      <div class="cell">Metasurface-based D-band demo</div>
      <div class="cell">Intelligent D-band Network Demo</div>
    </div>
    <div class="col kpi">
      <div class="head">Main KPIs</div>
      <div class="kpi-text">100 Gbps throughput · 100m range<br>Massive number of devices · Zero latency<br>Ultra-high reliability</div>
    </div>
  </div>

  <div class="concept-figure" role="img" aria-label="System concept diagram: key performance indicators, fundamental characteristics, enabling technologies, key technology modules and usage scenarios with small technical illustrations"></div>
</section>

</body>
</html>
```